Mango Grove Indian Restaurants 2019 Menu

Hi,
Please find attached menu text in pdf format. It contains 4 pages. Please work on the menu pages. I will further work with the winner to add the cover page and images as an extended project

Please visit www.mangogroveeats.com.au for more information

```html
<!DOCTYPE html>
<html lang="en">
<head>
<meta charset="utf-8">
<title>Mango Grove Menu Pages</title>
<link href="https://fonts.googleapis.com/css2?family=Montserrat:wght@400;500;600;700&family=Arvo:wght@700&display=swap" rel="stylesheet">
<style>
:root{
  --orange:#f7901e;
  --orange-text:#f07c1a;
  --ink:#1b1b1b;
  --paper:#ffffff;
  --backdrop:#e9e6e1;
  --brand:#c8201f;
}
*{margin:0;padding:0;box-sizing:border-box}
html,body{width:1200px;height:1200px;overflow:hidden;background:var(--backdrop)}
body{font-family:"Montserrat",sans-serif;color:var(--ink)}
.stage{position:relative;width:1500px;height:1500px;transform:scale(.8);transform-origin:0 0}
.sheet{position:absolute;background:var(--paper);box-shadow:0 6px 18px rgba(0,0,0,.18)}
.sheet-left{left:140px;top:128px;width:536px;height:780px}
.sheet-right{left:808px;top:588px;width:539px;height:779px}
.abs{position:absolute}
.frame{position:absolute;left:0;top:0;pointer-events:none}
.brand{position:absolute;transform:translateX(-50%);font-family:"Arvo",serif;font-weight:700;font-size:24px;color:var(--brand);white-space:nowrap;display:flex;align-items:center;gap:8px}
.brand-dot{width:12px;height:12px;border-radius:50%;background:var(--brand)}
.head-orange{color:var(--orange-text);font-weight:600;letter-spacing:.5px}
.slab{font-family:"Arvo",serif;font-weight:700;color:var(--orange-text)}
.rule{position:absolute;height:2px;background:var(--ink)}
.caps{text-transform:uppercase}
.tiny{font-size:7.5px;line-height:1.15}
.meat-list{list-style:none;font-size:10px;font-weight:700;letter-spacing:.6px;line-height:17px}
.toppings-band{position:absolute;left:0;top:338px;width:292px;height:212px;background:var(--orange)}
.topping{position:absolute;left:46px;font-size:9px;font-weight:700;letter-spacing:.4px;white-space:nowrap}
.topping-price{position:absolute;left:246px;font-size:13px;font-weight:600}
.item{position:absolute;left:331px;width:150px}
.item .price{font-size:17px;font-weight:700}
.item .name{font-size:9.5px;font-weight:600;color:var(--orange-text);letter-spacing:.5px;margin-top:4px;white-space:nowrap}
.item .name b{color:var(--ink)}
.item .desc{font-size:7.5px;line-height:13px;margin-top:2px;white-space:nowrap}
.breakfast-box{position:absolute;left:0;top:592px;width:211px;height:77px;background:var(--orange);padding:14px 0 0 42px}
.breakfast-box .price{font-size:20px;font-weight:700}
.breakfast-box .title{font-size:14px;font-weight:700;letter-spacing:.6px;line-height:14px}
.small-caps{font-variant:small-caps;font-size:9px;letter-spacing:.5px}
.opt{position:absolute;font-size:8px;line-height:13.5px}
.right{text-align:right}
.special-title{position:absolute;left:50%;transform:translateX(-50%);top:108px;font-size:23px;line-height:26px;background:var(--paper);padding:0 6px;white-space:nowrap}
.special-title span.bar{display:inline-block;width:18px;height:5px;border-top:2px solid var(--orange-text);border-bottom:2px solid var(--orange-text);vertical-align:middle;margin:0 4px}
.center{position:absolute;left:0;width:539px;text-align:center;white-space:nowrap}
.specials-band{position:absolute;left:50px;top:253px;width:439px;height:300px;background:var(--orange)}
.specials-band::after{content:"";position:absolute;inset:8px;border:2px solid var(--ink)}
.dish{position:absolute;left:82px;width:330px}
.dish .name{font-size:10px;font-weight:700;letter-spacing:.8px}
.dish .desc{font-size:7.3px;line-height:13px;margin-top:2px;white-space:nowrap}
.dish-price{position:absolute;left:420px;width:40px;text-align:right;font-size:13px;font-weight:600}
.tab{position:absolute;left:157px;top:576px;width:252px;height:37px;background:var(--orange);text-align:center;line-height:37px;font-size:12px;font-weight:600;letter-spacing:2px}
</style>
</head>
<body>
<div class="stage">

  <section class="sheet sheet-left" aria-label="Main menu page">
    <div class="brand" style="left:268px;top:26px"><span class="brand-dot"></span>Mango Grove</div>

    <div class="abs" style="left:45px;top:108px">
      <div class="head-orange" style="font-size:15px">CHOICE OF MEAT</div>
      <div class="tiny caps" style="width:180px">All tacos are served with cilantro and onions, unless told otherwise</div>
    </div>
    <div class="rule" style="left:48px;top:156px;width:47px"></div>
    <ul class="meat-list abs" style="left:46px;top:170px">
      <li>BISTEC</li><li>PASTOR</li><li>CHORIZO</li><li>CARNITAS</li><li>PICADILLO</li>
      <li>BARBACOA</li><li>CHICHARRON</li><li>SHREDDED CHICKEN</li><li>FAJITA (BEEF OR CHICKEN)</li>
    </ul>

    <svg class="frame" width="536" height="780" viewBox="0 0 536 780">
      <polyline points="236,576 236,110 446,110 488,156 488,576 236,576" fill="none" stroke="#1b1b1b" stroke-width="2"/>
      <polyline points="211,638 236,638 236,780" fill="none" stroke="#1b1b1b" stroke-width="2"/>
    </svg>

    <div class="toppings-band"></div>
    <div class="abs" style="left:46px;top:357px;font-size:13.5px;font-weight:600;letter-spacing:1px">ADDITIONAL TOPPINGS</div>
    <div class="rule" style="left:48px;top:387px;width:47px"></div>
    <div class="topping" style="top:404px">QUESO FRESCO</div><div class="topping-price" style="top:400px">$.25</div>
    <div class="topping" style="top:432px">AVOCADO</div><div class="topping-price" style="top:428px">$.25</div>
    <div class="topping" style="top:461px">SIDE OF RICE</div><div class="topping-price" style="top:457px;left:244px">$1.50</div>
    <div class="topping" style="top:489px">SIDE OF BEANS</div><div class="topping-price" style="top:485px;left:244px">$1.50</div>
    <div class="topping" style="top:518px">JALAPEÑO O SERRANO TOREADO</div><div class="topping-price" style="top:514px">$.50</div>

    <div class="slab abs" style="left:331px;top:126px;font-size:21px;line-height:25px">ITEM<br>CHOICE</div>
    <div class="rule" style="left:331px;top:181px;width:50px"></div>

    <div class="item" style="top:204px"><div class="price">$2.50</div><div class="name">TACO<b>: CORN OR FLOUR</b></div><div class="desc">served with cilantro and onion</div></div>
    <div class="item" style="top:269px"><div class="price">$5.00</div><div class="name">QUESADILLA</div><div class="desc">1 meat, salad, sour cream</div></div>
    <div class="item" style="top:334px"><div class="price">$6.00</div><div class="name">TORTA</div><div class="desc">1 meat, beans, let, tom, pickle jal,<br>avocado, sour cream</div></div>
    <div class="item" style="top:412px"><div class="price">$6.00</div><div class="name">BURRITO</div><div class="desc">1 meat, Beans, rice, lett, tom, pico,<br>sourcream, avoc, sauce</div></div>
    <div class="item" style="top:490px"><div class="price">$6.00</div><div class="name">BOWL</div><div class="desc">1 meat, rice, beans, salad,<br>sourcream, avoc, pico</div></div>

    <div class="breakfast-box">
      <div class="price">$1.50</div>
      <div class="title">BREAKFAST TACOS</div>
      <div class="small-caps" style="font-size:8.5px;line-height:9px">Flour or Corn Tortilla</div>
    </div>

    <div class="abs right" style="right:46px;top:604px">
      <div style="font-size:20px;font-weight:700;color:var(--orange-text)">$8.00</div>
      <div style="font-size:13px;font-weight:600;color:var(--orange-text);letter-spacing:1px;line-height:14px">LUNCH</div>
      <div class="small-caps">Plate (1 meat, rice beans, 3 tortillas, salad)</div>
    </div>

    <div class="abs small-caps" style="left:91px;top:686px;font-weight:700">Egg + 1 item</div>
    <div class="opt" style="left:42px;top:710px">Beans<br>Nopalitos<br>Chicharron</div>
    <div class="opt right" style="right:324px;top:710px">Sausage<br>Bacon Chorizo<br>Potatoes</div>

    <div class="abs small-caps" style="right:46px;top:686px;font-weight:700">Choice of meats</div>
    <div class="opt" style="left:288px;top:710px">Sausage<br>Bacon Chorizo<br>Potatoes</div>
    <div class="opt right" style="right:46px;top:710px">Fajita (beef or chicken)<br>Pastor<br>Chicharron</div>
  </section>

  <section class="sheet sheet-right" aria-label="Specials menu page">
    <div class="brand" style="left:267px;top:36px"><span class="brand-dot"></span>Mango Grove</div>

    <svg class="frame" width="539" height="779" viewBox="0 0 539 779">
      <polyline points="90,127 450,127 489,172 489,240 50,240 50,172 90,127" fill="none" stroke="#1b1b1b" stroke-width="2"/>
      <polyline points="50,779 50,595 157,595" fill="none" stroke="#1b1b1b" stroke-width="2"/>
      <polyline points="409,595 489,595 489,779" fill="none" stroke="#1b1b1b" stroke-width="2"/>
    </svg>
    <div class="special-title slab"><span class="bar"></span>SPECIAL<span class="bar"></span></div>
    <div class="center" style="top:148px;font-size:25px;font-weight:700">$7.00</div>
    <div class="center head-orange" style="top:183px;font-size:14px;letter-spacing:2px">TAQUITOS DE LA CASA</div>
    <div class="center" style="top:202px;font-size:6.5px;font-weight:600;font-variant:small-caps">5 Mini-Tacos, choice of up to two meats: Bistec (fine chopped steak), Pastor, Carnitas, Barbacoa o Chorizo</div>
    <div class="center" style="top:212px;font-size:7px">Small corn tortilla served with grilled onions, cilantro and raw onions</div>

    <div class="specials-band"></div>
    <div class="dish" style="top:276px"><div class="name">MATAMOROS STREET TACO</div><div class="desc">Corn tortilla, bistec (chopped steak), Grilled Onions, queso fresco, avocado,<br>house salsa, cilantro and onions.</div></div>
    <div class="dish-price" style="top:273px">$3.00</div>
    <div class="dish" style="top:339px"><div class="name">SAN FELIPE</div><div class="desc">Inhouse Carnitas served with special made Pico De Gallo traditionally served<br>In San Felipe Torres Mochas, Guanajuato.</div></div>
    <div class="dish-price" style="top:336px">$3.00</div>
    <div class="dish" style="top:402px"><div class="name">EL PASTOR</div><div class="desc">Inhouse Marinated Pork , served with cilantro, red onions, queso fresco and avocado.</div></div>
    <div class="dish-price" style="top:411px">$3.00</div>
    <div class="dish" style="top:451px"><div class="name">EL CAMPECHANO</div><div class="desc">Bistec (steak) , Chorizo , GRILLED nopalitos and onions served with cilantro and onions</div></div>
    <div class="dish-price" style="top:461px">$3.00</div>
    <div class="dish" style="top:501px"><div class="name">EL TEJANO</div><div class="desc">Beef Fajita, smoked sausage, grilled bell pepper, grilled onions and jalapeños</div></div>
    <div class="dish-price" style="top:510px">$3.00</div>

    <div class="tab">QUESADILLA / GRINGAS</div>
    <div class="dish" style="top:636px"><div class="name">GRINGA</div><div class="desc">Folded flour Tortilla stuffed with Melted Oaxaca, Azadero and Quesadilla<br>cheese topped with Pastor cilantro and onions</div></div>
    <div class="dish-price" style="top:633px">$3.50</div>
    <div class="dish" style="top:699px"><div class="name">SINCRONIZADA</div><div class="desc">Folded flour tortilla, grilled ham stuffed with melted Oaxaca, Azadero and<br>Quesadilla cheese, cilantro and onions</div></div>
    <div class="dish-price" style="top:696px">$3.50</div>
  </section>

</div>
</body>
</html>
```